Prime Match Sports Photo

I’m looking for an elite classy website where it talks a little bit about my experience and a video page and updates once a week of items I photo matched. I would like you to look at my three competitors for ideas on their sites I like them all. I photo match all professional sports game used equipment to the actual game they used it in.

```html
<!DOCTYPE html>
<html lang="en">
<head>
<meta charset="utf-8">
<title>Prime Match Sports Photo</title>
<link rel="stylesheet" href="https://fonts.googleapis.com/css2?family=Poppins:wght@600;700&family=Roboto:wght@400;500;700&display=swap">
<style>
:root{
  --navy:#0f2a63;
  --navy-deep:#0b1f4d;
  --red:#e5111f;
  --ink:#111111;
  --text:#555555;
  --muted:#777777;
  --white:#ffffff;
  --yellow:#f3c94a;
  --purple:#c78ad8;
}
*{box-sizing:border-box;margin:0;padding:0}
html,body{width:1200px;height:3965px;overflow:hidden}
body{font-family:"Roboto",sans-serif;color:var(--text);background:var(--white);position:relative}
.abs{position:absolute}
h1,h2{font-family:"Poppins",sans-serif;font-weight:700}

/* header */
.site-header{top:0;left:0;width:1200px;height:100px;background:var(--white)}
.brand{left:108px;top:30px;display:flex;align-items:center;gap:12px}
.brand-mark{width:44px;height:44px;background:var(--navy);border-radius:4px}
.brand-name{font-family:"Poppins",sans-serif;font-weight:700;font-size:16px;line-height:20px;color:var(--navy);width:150px}
.main-nav{left:364px;top:40px;display:flex;gap:19px;font-size:15px;font-weight:500;color:var(--ink)}
.main-nav a{color:inherit;text-decoration:none;padding-bottom:8px}
.main-nav a.active{color:var(--navy);border-bottom:3px solid var(--navy)}
.btn{display:inline-flex;align-items:center;justify-content:center;gap:8px;background:var(--red);color:var(--white);font-weight:700;text-decoration:none;border-radius:30px;text-transform:uppercase}
.btn-submit{left:908px;top:28px;width:180px;height:44px;font-size:15px}

/* bands */
.band{left:0;width:1200px;color:var(--white);text-align:center}
.band-bg{position:absolute;inset:0}
.band-inner{position:relative;padding:0 210px}
.band h1{font-size:36px;line-height:42px;text-transform:uppercase}
.band h2{font-size:34px;line-height:40px;text-transform:uppercase}
.band p{font-size:15px;line-height:26px}
.hero{top:100px;height:540px}
.hero .band-inner{padding-top:136px}
.hero p{font-size:16.5px;line-height:28px;margin-top:26px;font-weight:500}
.btn-quote{width:208px;height:54px;font-size:16px;margin-top:34px}
.value-band{top:1326px;height:275px}
.value-band .band-inner,.about-band .band-inner{padding-top:80px}
.value-band p,.about-band p{margin-top:14px}
.about-band{top:2664px;height:274px}
.arrow{width:16px;height:16px}

/* offer */
.offer-photo{left:111px;top:753px;width:489px;height:456px;background:linear-gradient(135deg,#e6c842 0%,#caa52a 55%,#6d6a52 100%)}
.offer-badge{left:465px;top:866px;width:186px;height:231px;border-radius:115px 0 0 115px;background:var(--white)}
.offer-shirt{left:500px;top:885px;width:150px;height:190px;background:linear-gradient(180deg,#f4dc34,#e9c81e);border-radius:10px}
.offer{left:718px;top:772px;width:380px}
.offer h2{font-size:30px;color:var(--ink);text-transform:uppercase;margin-bottom:24px}
.offer-list{list-style:none;position:relative}
.offer-list::before{content:"";position:absolute;left:14px;top:14px;height:240px;width:2px;background:#7a1b1b}
.offer-item{position:relative;padding-left:54px;margin-bottom:25px}
.offer-num{position:absolute;left:0;top:0;width:30px;height:30px;border-radius:50%;border:3px solid;font-size:13px;display:flex;align-items:center;justify-content:center;color:var(--ink)}
.n1{border-color:var(--yellow);background:#fce29a}.n2{border-color:#f06b6b;background:#ee3b3b}.n3{border-color:var(--purple);background:#d9a9e6}
.offer-item h3{font-size:17px;font-weight:500;color:var(--ink);line-height:30px}
.offer-item p{font-size:14px;line-height:20px;color:var(--muted)}

/* cards */
.cards{left:111px;top:1654px;display:flex;gap:18px}
.card{width:231px;height:278px;background:var(--white);box-shadow:0 0 8px rgba(0,0,0,.15);text-align:center;padding-top:10px}
.card-art{width:110px;height:132px;margin:0 auto;border-radius:8px}
.art-red{background:linear-gradient(135deg,#d2101a,#1a1a1a)}
.art-bat{background:linear-gradient(135deg,#fff,#dcb27a 50%,#fff)}
.art-black{background:linear-gradient(180deg,#1b1b1b,#333 70%,#e45a1b)}
.art-lime{background:linear-gradient(135deg,#1a1a1a 50%,#b7de2b)}
.card h3{font-size:19px;font-weight:500;color:var(--ink);margin-top:14px}
.card p{font-size:13.5px;line-height:22px;color:var(--muted);margin-top:10px;padding:0 18px}

/* video */
.video-title{left:0;top:2040px;width:1200px;text-align:center;font-size:33px;color:var(--ink)}
.video{left:162px;top:2125px;width:876px;height:425px;padding:5px;background:var(--white);box-shadow:0 0 8px rgba(0,0,0,.2)}
.video-still{width:100%;height:100%;background:linear-gradient(135deg,#7c8a6c,#b8433e 45%,#e5e0dc 65%,#5e6a3e)}
.play{left:565px;top:2303px;width:70px;height:70px}

/* photomatch */
.match{left:112px;top:3038px;width:450px}
.match h2{font-size:33px;color:var(--ink);text-transform:uppercase}
.match p{font-size:15.5px;line-height:26px;color:var(--text);margin-top:26px}
.btn-read{left:112px;top:3430px;width:155px;height:45px;font-size:15px}
.match-frame{left:700px;top:3028px;width:386px;height:489px;border:7px solid var(--navy)}
.match-photo{left:610px;top:3037px;width:468px;height:473px;background:linear-gradient(180deg,#ddd9e4 0%,#c9c7cc 40%,#2b4a2e 70%,#3c3a33 100%)}

/* footer */
.site-footer{left:0;top:3648px;width:1200px;height:317px;background:var(--navy-deep);color:var(--white)}
.fcol{position:absolute;top:60px}
.fcol h4{font-size:16px;font-weight:500;text-transform:uppercase;margin-bottom:16px}
.fcol ul{list-style:none;font-size:12px;line-height:22px}
.fdiv{position:absolute;top:60px;width:1px;height:150px;background:rgba(255,255,255,.12)}
.contact li{display:flex;gap:14px;align-items:flex-start;margin-bottom:6px}
.contact svg{flex:none;margin-top:4px}
.social li{display:flex;align-items:center;gap:14px;margin-bottom:8px}
.dot{width:28px;height:28px;border-radius:50%;background:var(--red)}
.copyright{position:absolute;left:0;top:278px;width:1200px;text-align:center;font-size:11px}
</style>
</head>
<body>

<header class="site-header abs">
  <div class="brand abs"><span class="brand-mark"></span><span class="brand-name">Prime Match Sports Photo</span></div>
  <nav class="main-nav abs">
    <a class="active" href="#">Home</a><a href="#">About Us</a><a href="#">Value of Our Photomatch</a><a href="#">The Process</a><a href="#">Contact Us</a>
  </nav>
  <a class="btn btn-submit abs" href="#">Submit an Item</a>
</header>

<section class="band hero abs">
  <div class="band-bg" role="img" aria-label="Dark blue tinted photo of a football player in action" style="background:linear-gradient(135deg,#17336f,#1d3c80 50%,#122a60)"></div>
  <div class="band-inner">
    <h1>The Leader in Game Used<br>Photomatching!</h1>
    <p>Sed ut perspiciatis unde omnis iste natus error sit voluptatem accusantium doloremque laudantium, totam rem aperiam, eaque ipsa quae ab illo inventore veritatis et quasi architecto</p>
    <a class="btn btn-quote" href="#">Get a Quote
      <svg class="arrow" viewBox="0 0 16 16"><circle cx="8" cy="8" r="7" fill="#fff"/><path d="M6 4.5 9.5 8 6 11.5" stroke="#e5111f" stroke-width="2" fill="none"/></svg></a>
  </div>
</section>

<div class="offer-photo abs" role="img" aria-label="Back of a yellow number 10 football shirt worn by a fan"></div>
<div class="offer-badge abs"></div>
<div class="offer-shirt abs" role="img" aria-label="Yellow number 10 football jersey"></div>
<section class="offer abs">
  <h2>What We Offer:</h2>
  <ol class="offer-list">
    <li class="offer-item"><span class="offer-num n1">1</span><h3>The Most Thorough Search:</h3><p>Lorem ipsum dolor sit amet, adipiscing elit, sed do eiusmod incididunt ut labore et dolore magna aliqua.</p></li>
    <li class="offer-item"><span class="offer-num n2">2</span><h3>Experience:</h3><p>Lorem ipsum dolor sit amet, adipiscing elit, sed do eiusmod incididunt ut labore et dolore magna aliqua.</p></li>
    <li class="offer-item"><span class="offer-num n3">3</span><h3>Guaranteed Best Price:</h3><p>Lorem ipsum dolor sit amet, adipiscing elit, sed do eiusmod incididunt ut labore et dolore magna aliqua.</p></li>
  </ol>
</section>

<section class="band value-band abs">
  <div class="band-bg" role="img" aria-label="Dark blue tinted stadium photo with a player in a white jersey" style="background:linear-gradient(90deg,#132a5c,#24386a 50%,#5a6478 75%,#1c2f5e)"></div>
  <div class="band-inner">
    <h2>Value of Our Photomatch</h2>
    <p>Sed ut perspiciatis unde omnis iste natus error sit voluptatem accusantium doloremque laudantium, totam rem aperiam, eaque ipsa quae ab illo inventore veritatis et quasi architecto</p>
  </div>
</section>

<div class="cards abs">
  <article class="card"><div class="card-art art-red" role="img" aria-label="Red and black sports jersey"></div><h3>Lorem ipsum dolor sit</h3><p>Sed ut perspiciatis unde omnis iste natus error sit voluptatem accusantium doloremque</p></article>
  <article class="card"><div class="card-art art-bat" role="img" aria-label="Wooden baseball bat and ball"></div><h3>Lorem ipsum dolor sit</h3><p>Sed ut perspiciatis unde omnis iste natus error sit voluptatem accusantium doloremque</p></article>
  <article class="card"><div class="card-art art-black" role="img" aria-label="Black number 10 football jersey"></div><h3>Lorem ipsum dolor sit</h3><p>Sed ut perspiciatis unde omnis iste natus error sit voluptatem accusantium doloremque</p></article>
  <article class="card"><div class="card-art art-lime" role="img" aria-label="Black and lime green sports jersey"></div><h3>Lorem ipsum dolor sit</h3><p>Sed ut perspiciatis unde omnis iste natus error sit voluptatem accusantium doloremque</p></article>
</div>

<h2 class="video-title abs">OUR VIDEO</h2>
<div class="video abs"><div class="video-still" role="img" aria-label="American football players tackling during a game"></div></div>
<svg class="play abs" viewBox="0 0 70 70"><circle cx="35" cy="35" r="33" fill="#1e8be0" stroke="#fff" stroke-width="3"/><path d="M27 20 51 35 27 50Z" fill="#fff"/></svg>

<section class="band about-band abs">
  <div class="band-bg" role="img" aria-label="Dark blue tinted stadium photo with a helmeted player" style="background:linear-gradient(90deg,#142d63,#1f3a77 60%,#3b4f80 85%,#1d3570)"></div>
  <div class="band-inner">
    <h2>About Us</h2>
    <p>Sed ut perspiciatis unde omnis iste natus error sit voluptatem accusantium doloremque laudantium, totam rem aperiam, eaque ipsa quae ab illo inventore veritatis et quasi architecto</p>
  </div>
</section>

<section class="match abs">
  <h2>What is a Photomatch?</h2>
  <p>Lorem ipsum dolor sit amet, consectetur adipiscing elit, sed do eiusmod tempor incididunt ut labore et dolore magna aliqua. Ut enim ad minim veniam, quis nostrud exercitation ullamco laboris nisi ut aliquip ex ea commodo consequat. Duis aute irure dolor in reprehenderit in voluptate velit esse cillum dolore eu fugiat nulla pariatur.</p>
  <p>Sed ut perspiciatis unde omnis iste natus error sit voluptatem accusantium doloremque laudantium, totam rem aperiam, eaque ipsa quae ab illo inventore veritatis et quasi architecto beatae vitae dicta sunt explicabo.</p>
</section>
<a class="btn btn-read abs" href="#">Read More
  <svg class="arrow" viewBox="0 0 16 16"><circle cx="8" cy="8" r="7" fill="#fff"/><path d="M6 4.5 9.5 8 6 11.5" stroke="#e5111f" stroke-width="2" fill="none"/></svg></a>
<div class="match-frame abs"></div>
<div class="match-photo abs" role="img" aria-label="Football team in green jerseys huddled together"></div>

<footer class="site-footer abs">
  <div class="fcol" style="left:113px"><h4>Quick Links</h4><ul><li>Home</li><li>About Us</li><li>Value of Our Photomatch</li><li>The Process</li><li>Portfolio</li></ul></div>
  <div class="fdiv" style="left:271px"></div>
  <div class="fcol" style="left:349px"><h4>Information</h4><ul><li>Terms &amp; Conditions</li><li>Privacy Policy</li><li>Disclaimer</li><li>Site Map</li><li>Contact Us</li></ul></div>
  <div class="fdiv" style="left:536px"></div>
  <div class="fcol" style="left:614px;width:200px"><h4>Contact Info</h4>
    <ul class="contact">
      <li><svg width="12" height="12" viewBox="0 0 12 12"><rect x="1" y="2" width="10" height="8" rx="2" fill="#e5111f"/></svg>(555) 014-2200</li>
      <li><svg width="12" height="12" viewBox="0 0 12 12"><rect x="1" y="3" width="10" height="7" rx="2" fill="#e5111f"/></svg>(555) 014-2200</li>
      <li><svg width="12" height="12" viewBox="0 0 12 12"><rect x="1" y="2" width="10" height="8" fill="#e5111f"/><path d="M1 2 6 7 11 2" stroke="#0b1f4d" fill="none"/></svg><u>hello@primematch.example</u></li>
      <li><svg width="12" height="12" viewBox="0 0 12 12"><path d="M6 11C3 7 2 5.5 2 4.5a4 4 0 0 1 8 0C10 5.5 9 7 6 11Z" fill="#e5111f"/></svg><span style="line-height:14px">Suite 40, 12 Harbor Lane, Fairview</span></li>
    </ul></div>
  <div class="fdiv" style="left:876px"></div>
  <div class="fcol" style="left:953px"><h4>Follow Us</h4>
    <ul class="social"><li><span class="dot"></span>Feed</li><li><span class="dot"></span>Chirp</li><li><span class="dot"></span>Circles</li><li><span class="dot"></span>Careers</li></ul></div>
  <p class="copyright">Copyrights © The Company name 2020 | Allrights Reserved</p>
</footer>

</body>
</html>
```